International car care products company needs new concept package design.

Our company is called Corvane Motor Tonics and we are expanding to the power sports market. So we are looking for someone to design our new bottle labels. We have always been inspired by the beverage and wine markets packaging. We need a cohesive look using bold colors and graphic's that will attract attention yet not be overly busy or say "me too" the labels need to have some copy that instantly lets someone know what the product is for and why it is different but is still clean. We have uploaded some mock up labels and also some inspiration of products we love. the product will be called Corvane "K " Series. The G standing for Graphene.

```html
<!DOCTYPE html>
<html lang="en">
<head>
<meta charset="utf-8">
<title>Corvane K Series Instant Detailer Label</title>
<link rel="stylesheet" href="https://fonts.googleapis.com/css2?family=Oswald:wght@700&family=Open+Sans:wght@600;700&display=swap">
<style>
  :root {
    --label-black: #0d0d0d;
    --label-red: #a8131a;
    --label-red-text: #c4161c;
    --label-yellow: #d9d421;
    --label-white: #f2f2f2;
    --emblem-tone: #1c1c1c;
    --page-bg: #ffffff;
  }
  html, body {
    margin: 0;
    padding: 0;
    width: 1200px;
    height: 1200px;
    overflow: hidden;
    background: var(--page-bg);
  }
  .canvas {
    position: relative;
    width: 1200px;
    height: 1200px;
  }
  .product-label {
    position: absolute;
    left: 368px;
    top: 40px;
    width: 463px;
    height: 1120px;
  }
  .brand-name {
    font-family: "Open Sans", sans-serif;
    font-weight: 600;
    fill: var(--label-white);
  }
  .claim-line {
    font-family: "Oswald", sans-serif;
    font-weight: 700;
    fill: var(--label-red-text);
  }
  .product-type {
    font-family: "Oswald", sans-serif;
    font-weight: 700;
    fill: var(--label-black);
  }
  .volume-text {
    font-family: "Open Sans", sans-serif;
    font-weight: 700;
    fill: var(--label-white);
  }
  .fill-black { fill: var(--label-black); }
  .fill-red { fill: var(--label-red); }
  .fill-yellow { fill: var(--label-yellow); }
  .fill-emblem { fill: var(--emblem-tone); }
</style>
</head>
<body>
<main class="canvas">
  <svg class="product-label" viewBox="0 0 430 1040" xmlns="http://www.w3.org/2000/svg" aria-label="Corvane K Series graphene infused instant detailer label">
    <rect class="fill-black" x="0" y="0" width="430" height="1040"/>

    <path class="fill-red side-panels" role="img" aria-label="Red textured side panels"
          d="M0 300 C100 380 170 470 215 560 C260 470 330 380 430 300 L430 1040 L0 1040 Z"/>

    <path class="fill-yellow lower-arch"
          d="M0 740 C60 640 140 575 215 565 C290 575 370 640 430 740 L430 1040 L0 1040 Z"/>

    <text class="brand-name" x="215" y="245" text-anchor="middle" font-size="58">Corvane</text>

    <circle class="fill-emblem series-emblem" cx="212" cy="475" r="172" role="img" aria-label="K Series emblem placeholder"/>

    <text class="claim-line" x="215" y="726" text-anchor="middle" font-size="62" textLength="356" lengthAdjust="spacingAndGlyphs">GRAPHENE INFUSED</text>
    <text class="product-type" x="215" y="818" text-anchor="middle" font-size="92" textLength="400" lengthAdjust="spacingAndGlyphs">INSTANT DETAILER</text>

    <path class="fill-black volume-tag" d="M172 972 L215 944 L258 972 L258 1040 L172 1040 Z"/>
    <text class="volume-text" x="215" y="1007" text-anchor="middle" font-size="19" letter-spacing="1">16 OZ</text>
  </svg>
</main>
</body>
</html>
```